Golden Meadow Pie House site. I'm opening up a shop in a few months and I have ideas of what I want,

I would like a wordpress design that is mobile friendly. I want to be able to easily add and remove photos when necessary. I want to be able to display my home, about us, contact us, instagram photos, and my menu. I need to eventually include the days and hours the store will be open. I would like to also include the instagram and FB symbol (I know there is a name for it, not sure) that will take you directly to the site.

Please look at the following sites. I like the simplicity of it. I've attached a picture below that shows how I told my logo designer I would like my font.

https://www.cornerfernkitchen.example/
https://www.thetinycrumbles.example/
http://www.sevenbrotherspastry.example/
Below is my instagram page

https://www.snapgrid.example/goldenmeadowpiehouse/

Target Market(s)

All ages

Industry/Entity Type

Bakery

Coding

Coded - Design and coding required

Font styles to use
Serif
Sans Serif

Colors
9d9d9d
757575
474747
fbd4d5

Requirements
Must have
• I've attached my updated logo. Please use it when making the website. Thank you. Keep colors simple. Remember, my bakery is going to have a rustic theme. I've attached my "About Us", please include. I crossed out what I don't want included. Thanks!! :)
Nice to have
• See websites I've attached for ideas. Can't wait to see some designs! Clean borders for pictures, preferably squares. I like the pink, but please, I don't want it to be all you see. Very minimal. I could see some designs without as well. Think rustic chic, simple, elegant. Hope that helps!
Should not have
• I don't want my website to look exactly like the examples. :) No scallop edges. I do not sell online.

```html
<!DOCTYPE html>
<html lang="en">
<head>
<meta charset="utf-8">
<title>Golden Meadow Pie House</title>
<link href="https://fonts.googleapis.com/css2?family=Lobster&family=Source+Sans+3:wght@400;600&display=swap" rel="stylesheet">
<style>
:root{
  --pink:#fbd4d5;
  --tan:#b48a68;
  --tan-dark:#a57656;
  --ink:#2b2b2b;
  --grey-dark:#474747;
  --grey:#757575;
  --grey-light:#9d9d9d;
  --night:#1e2022;
  --white:#ffffff;
  --script:"Lobster", cursive;
  --sans:"Source Sans 3", "Source Sans Pro", sans-serif;
}
*{margin:0;padding:0;box-sizing:border-box}
html,body{width:1200px;height:3020px;overflow:hidden;background:var(--white)}
body{position:relative;font-family:var(--sans);color:var(--grey-dark)}
.fill{position:absolute}

/* header */
.site-header{position:absolute;left:0;top:0;width:1200px;height:52px;background:var(--white);border-bottom:3px solid var(--pink);z-index:3}
.nav-link{position:absolute;top:18px;font-family:var(--script);font-size:13px;color:var(--ink)}
.nav-link.is-active{color:var(--tan)}
.brand-badge{position:absolute;left:498px;top:0;width:204px;height:102px;background:var(--white);border:2px solid var(--pink);border-top:none;border-radius:0 0 40px 40px;z-index:4;display:flex;align-items:center;justify-content:center;text-align:center}
.brand-name{font-family:var(--script);font-size:20px;line-height:1.15;color:var(--grey-dark)}

/* hero */
.hero{position:absolute;left:0;top:52px;width:1200px;height:435px;background:radial-gradient(ellipse at 55% 55%,#7a5236 0%,#4c3424 40%,#8a8178 75%,#cfccc7 100%)}
.hero-title{position:absolute;top:185px;width:100%;text-align:center;font-family:var(--script);font-weight:400;font-size:50px;color:var(--white)}
.divider{position:absolute;display:flex;align-items:center;justify-content:center;gap:6px}
.divider i{display:block;width:22px;height:1px;background:currentColor}
.divider b{display:block;width:8px;height:8px;border:1px solid currentColor;border-radius:50%}

/* section titles */
.section-title{position:absolute;width:100%;text-align:center;font-family:var(--script);font-weight:400;font-size:21px;letter-spacing:1px;color:var(--ink);text-transform:uppercase}

/* about */
.about-photo-main{left:244px;top:531px;width:304px;height:422px;background:linear-gradient(135deg,#5e4a35,#7b6a55 45%,#2f3b55 75%,#e5e1db);box-shadow:0 6px 16px rgba(0,0,0,.15)}
.about-photo-cake{left:586px;top:810px;width:370px;height:212px;background:radial-gradient(ellipse at 45% 50%,#efece6 0%,#c8b69c 35%,#5c4634 80%);box-shadow:0 6px 16px rgba(0,0,0,.12)}
.about-heading{position:absolute;left:586px;top:563px;font-family:var(--script);font-weight:400;font-size:19px;color:var(--ink)}
.about-lead{position:absolute;left:586px;top:628px;font-size:12px;font-weight:600;color:var(--ink)}
.about-body{position:absolute;left:586px;top:656px;width:370px;font-size:11.5px;line-height:1.75;color:var(--grey)}
.btn-outline{position:absolute;display:flex;align-items:center;justify-content:center;border:1px solid var(--grey-dark);font-size:9px;letter-spacing:.5px;text-transform:uppercase}
.btn-more{left:586px;top:740px;width:106px;height:30px;color:var(--grey-dark)}

/* menu */
.menu-section{position:absolute;left:0;top:1066px;width:1200px;height:560px;background:var(--night)}
.menu-section .section-title{color:var(--white);top:36px}
.menu-tabs{position:absolute;top:108px;left:0;width:100%;display:flex;justify-content:center}
.menu-tab{font-size:13px;letter-spacing:.6px;color:var(--white);padding:0 32px;border-left:1px solid #6d6d6d;text-transform:uppercase}
.menu-tab:first-child{border-left:none}
.menu-tab.is-active{color:var(--tan)}
.menu-item{position:absolute;width:290px}
.menu-item h3{font-family:var(--script);font-weight:400;font-size:13px;color:var(--white);margin-bottom:9px}
.menu-item p{font-size:11px;line-height:1.7;color:#d8d8d8}
.btn-menu{left:546px;top:484px;width:106px;height:28px;border-color:var(--tan);color:var(--tan)}
.beans-deco{left:1080px;top:0;width:120px;height:150px;background:radial-gradient(circle at 70% 30%,#8a5533 0%,#5a3a24 35%,rgba(30,32,34,0) 70%)}

/* contact */
.field{position:absolute;border:1px solid var(--grey-dark);background:var(--white);font-size:10.5px;color:var(--grey);padding:8px 8px}
.btn-send{position:absolute;left:546px;top:1978px;width:82px;height:30px;background:var(--tan-dark);color:var(--white);font-size:9px;letter-spacing:.5px;display:flex;align-items:center;justify-content:center}
.spoon-deco{left:920px;top:1735px;width:230px;height:318px;background:radial-gradient(ellipse at 35% 30%,#b07a52 0%,#e5c7a3 35%,rgba(255,255,255,0) 70%)}

/* map + hours */
.map-area{left:0;top:2052px;width:1200px;height:388px;background:linear-gradient(180deg,#ececea,#e2e2df)}
.hours-card{position:absolute;left:244px;top:2115px;width:226px;height:260px;background:var(--white);box-shadow:0 4px 14px rgba(0,0,0,.18);text-align:center}
.hours-card h2{font-family:var(--script);font-weight:400;font-size:19px;color:var(--ink);margin-top:42px;text-transform:uppercase}
.hours-day{font-size:13px;font-weight:600;color:var(--ink)}
.hours-time{font-size:13px;color:var(--grey-dark)}

/* instagram */
.insta-tile{position:absolute;top:2548px;width:164px;height:164px}
.insta-count{position:absolute;top:72px;color:var(--white);font-size:12px;display:flex;align-items:center;gap:4px}

/* footer */
.site-footer{position:absolute;left:0;top:2755px;width:1200px;height:265px;background:#232323}
.footer-badge{position:absolute;left:500px;top:0;width:200px;height:120px;background:var(--white);border-radius:0 0 40px 40px;display:flex;align-items:center;justify-content:center;text-align:center}
.footer-text{position:absolute;top:157px;font-size:11px;line-height:1.9;color:#e6e6e6}
.footer-rule{position:absolute;left:244px;top:232px;width:712px;height:1px;background:#555}
.copyright{position:absolute;left:244px;top:243px;font-size:9.5px;color:#cfcfcf}
.social-dot{position:absolute;top:244px;width:9px;height:9px;border-radius:50%;background:#e6e6e6}
</style>
</head>
<body>

<header class="site-header">
  <a class="nav-link is-active" style="left:290px">Home</a>
  <a class="nav-link" style="left:346px">About Us</a>
  <a class="nav-link" style="left:418px">Location</a>
  <a class="nav-link" style="left:726px">Menu</a>
  <a class="nav-link" style="left:780px">Instagram</a>
  <a class="nav-link" style="left:858px">Contact Us</a>
</header>
<div class="brand-badge"><span class="brand-name">Golden Meadow<br>Pie House</span></div>

<section class="hero" role="img" aria-label="Close-up photo of chocolate chip cookies with a glass of milk">
  <h1 class="hero-title">Made With Love</h1>
  <div class="divider" style="left:0;width:100%;top:283px;color:#fff"><i></i><b></b><i></i></div>
</section>

<section class="about">
  <div class="fill about-photo-main" role="img" aria-label="Photo of the baker at a window holding a white cake with a pink rose"></div>
  <h2 class="about-heading">ABOUT US</h2>
  <div class="divider" style="left:586px;top:597px;color:var(--grey-dark)"><i></i><b></b><i></i></div>
  <p class="about-lead">Hey there and welcome to Golden Meadow Pie House!</p>
  <p class="about-body">My passion for baking at home for my children has flourished into my bake shop. I guess you can call me a mom-preneur. I'm so thankful for the great support of my husband and children - that's all of us on the right.</p>
  <a class="btn-outline btn-more">More About</a>
  <div class="fill about-photo-cake" role="img" aria-label="Photo of a white frosted cake topped with a pink rose on a gold stand"></div>
</section>

<section class="menu-section">
  <div class="fill beans-deco" role="img" aria-label="Scattered coffee beans"></div>
  <h2 class="section-title">Our Menu</h2>
  <div class="divider" style="left:0;width:100%;top:74px;color:#fff"><i></i><b></b><i></i></div>
  <nav class="menu-tabs">
    <span class="menu-tab is-active">Cakes</span>
    <span class="menu-tab">Cup Cakes</span>
    <span class="menu-tab">Bars</span>
    <span class="menu-tab">Cookies</span>
    <span class="menu-tab">Confections</span>
    <span class="menu-tab">Cake Donuts</span>
  </nav>
  <div class="menu-item" style="left:244px;top:160px"><h3>*Chocolate Salted Caramel</h3><p>Moist chocolate cake frosted with salted caramel buttercream and salted caramel drizzle</p></div>
  <div class="menu-item" style="left:244px;top:238px"><h3>Red Velvet</h3><p>Classic southern red velvet cake frosted with cream cheese buttercream</p></div>
  <div class="menu-item" style="left:244px;top:316px"><h3>*Cookies &amp; Cream</h3><p>Chocolate cake frosted with cookies and cream buttercream</p></div>
  <div class="menu-item" style="left:244px;top:380px"><h3>Classic Vanilla Bean</h3><p>Moist vanilla cake frosted with vanilla bean or chocolate buttercream</p></div>
  <div class="menu-item" style="left:668px;top:160px"><h3>Chocolate Cake</h3><p>Moist chocolate cake frosted with chocolate or vanilla buttercream</p></div>
  <div class="menu-item" style="left:668px;top:238px"><h3>*Hummingbird</h3><p>Banana, pecan and pineapple cake frosted with brown buttercream</p></div>
  <div class="menu-item" style="left:668px;top:316px"><h3>Classic Carrot</h3><p>Carrot cake with cinnamon cream cheese buttercream</p></div>
  <div class="menu-item" style="left:668px;top:380px"><h3>*Sticky Toffee Pudding</h3><p>Date cake frosted with mascarpone whipped cream, and topped with toffee sauce</p></div>
  <a class="btn-outline btn-menu">View All Menu</a>
</section>

<section class="contact">
  <h2 class="section-title" style="top:1661px">Contact Us</h2>
  <div class="divider" style="left:0;width:100%;top:1701px;color:var(--grey-dark)"><i></i><b></b><i></i></div>
  <div class="field" style="left:288px;top:1733px;width:306px;height:32px">Your Name</div>
  <div class="field" style="left:606px;top:1733px;width:306px;height:32px">Your Email</div>
  <div class="field" style="left:288px;top:1783px;width:306px;height:32px">Your Phone</div>
  <div class="field" style="left:606px;top:1783px;width:306px;height:32px">Your Subject</div>
  <div class="field" style="left:288px;top:1833px;width:624px;height:108px">Your Message</div>
  <a class="btn-send">SEND</a>
  <div class="fill spoon-deco" role="img" aria-label="Wooden spoon filled with coffee beans"></div>
</section>

<section class="location">
  <div class="fill map-area" role="img" aria-label="Street map of the area around the shop"></div>
  <div class="hours-card">
    <h2>Opening Hours</h2>
    <div class="divider" style="left:0;width:100%;top:80px;color:var(--grey-dark)"><i></i><b></b><i></i></div>
    <p class="hours-day" style="margin-top:34px">Monday - Friday</p>
    <p class="hours-time" style="margin-top:13px">8:00 am - 8:30 pm</p>
    <p class="hours-day" style="margin-top:13px">Saturday - Sunday</p>
    <p class="hours-time" style="margin-top:13px">10:00 am - 16:30 pm</p>
  </div>
</section>

<section class="instagram">
  <h2 class="section-title" style="top:2476px">Instagram</h2>
  <div class="divider" style="left:0;width:100%;top:2516px;color:var(--grey-dark)"><i></i><b></b><i></i></div>
  <div class="insta-tile" style="left:244px;background:radial-gradient(circle,#f3efe8,#d9cfc2)" role="img" aria-label="Photo of white frosted cookies with sprinkles"></div>
  <div class="insta-tile" style="left:426px;background:linear-gradient(135deg,#3a2319,#1d100b)" role="img" aria-label="Photo of chocolate brownies">
    <span class="insta-count" style="left:58px">
      <svg width="12" height="11" viewBox="0 0 12 11"><path d="M6 10 L1.2 5.2 A2.6 2.6 0 0 1 6 2 A2.6 2.6 0 0 1 10.8 5.2 Z" fill="none" stroke="#fff" stroke-width="1.2"/></svg>15
    </span>
    <span class="insta-count" style="left:98px">
      <svg width="12" height="12" viewBox="0 0 12 12"><circle cx="6" cy="5.5" r="4.5" fill="none" stroke="#fff" stroke-width="1.2"/></svg>0
    </span>
  </div>
  <div class="insta-tile" style="left:608px;background:linear-gradient(135deg,#e8e2da,#8d7560)" role="img" aria-label="Photo of sliced pie bars"></div>
  <div class="insta-tile" style="left:792px;background:linear-gradient(180deg,#ecebe9,#c9b8a8)" role="img" aria-label="Photo of a child holding two frosted donuts"></div>
</section>

<footer class="site-footer">
  <div class="footer-badge"><span class="brand-name">Golden Meadow<br>Pie House</span></div>
  <p class="footer-text" style="left:420px;text-align:right;width:170px">Lorem Ipsum is simply dummy text of the printing and type.</p>
  <p class="footer-text" style="left:610px"><strong>EMAIL :</strong> info@goldenmeadowpiehouse.example<br><strong>PHONE :</strong> +1 555 0148 392</p>
  <div class="footer-rule"></div>
  <p class="copyright">© 2017 GOLDEN MEADOW</p>
  <span class="social-dot" style="left:914px"></span>
  <span class="social-dot" style="left:940px"></span>
</footer>

</body>
</html>
```